Brightwell Essence colloidal silver spray for pets.

We need a label for an 8-oz cobalt blue spray bottle. We are a small company just starting to share the benefits of colloidal silver. Our first offering will be the 8-oz spray bottle for pets. We would also like to update our logo. The finished project should be crisp and incorporate a dog on the label. I have attached the information we would like on the label and our logo, which can be changed to match your vision.
Updates

Hi, I would like to remind you that we are using a cobalt blue bottle with a black sprayer and would like an updated logo. Also, for the business cards, we don't want an animal on them, as we are planning future products for people. thank you

```html
<!DOCTYPE html>
<html lang="en">
<head>
<meta charset="utf-8">
<title>Brightwell Essence – Colloidal Silver Label</title>
<link href="https://fonts.googleapis.com/css2?family=Fredoka:wght@500;600&family=Rye&family=Roboto:wght@400&display=swap" rel="stylesheet">
<style>
  :root{
    --bg-light:#f2f2f2;
    --bg-dark:#cfcfcf;
    --brand-teal:#1f9bb4;
    --dim-blue:#2b6fa8;
    --title-green:#0b8a43;
    --title-outline:#ffffff;
    --badge-navy:#2c3290;
    --white:#ffffff;
    --flag-red:#e0222b;
    --photo-top:#8a873c;
    --photo-mid:#a3a252;
    --photo-low:#95a23a;
    --photo-grass:#b3b52c;
    --coat-cream:#f1e6d2;
    --coat-tan:#d9a466;
  }
  *{margin:0;padding:0;box-sizing:border-box;}
  html,body{width:1200px;height:1200px;overflow:hidden;}
  body{
    background:radial-gradient(ellipse at 55% 50%,var(--bg-light) 0%,var(--bg-dark) 100%);
    position:relative;
    font-family:"Fredoka",sans-serif;
  }

  /* dimension markers */
  .dimension{position:absolute;color:var(--dim-blue);font-family:"Roboto",sans-serif;font-size:30px;font-weight:400;}
  .dimension svg{position:absolute;left:0;top:0;overflow:visible;}
  .dimension-width{left:160px;top:100px;width:440px;height:40px;}
  .dimension-width .dimension-value{position:absolute;left:0;right:0;top:2px;text-align:center;}
  .dimension-height{left:90px;top:170px;width:40px;height:922px;}
  .dimension-height .dimension-value{position:absolute;left:50%;top:50%;transform:translate(-50%,-50%) rotate(-90deg);white-space:nowrap;}

  /* label */
  .label{position:absolute;left:160px;top:170px;width:440px;height:922px;overflow:hidden;}
  .label-backdrop{
    position:absolute;inset:0;
    background:linear-gradient(180deg,var(--photo-top) 0%,var(--photo-mid) 32%,var(--photo-low) 62%,var(--photo-grass) 100%);
  }
  .label-photo{
    position:absolute;left:0;right:0;top:505px;bottom:0;
    background:
      radial-gradient(ellipse 34% 36% at 50% 52%,var(--coat-cream) 0%,rgba(241,230,210,.85) 45%,rgba(241,230,210,0) 100%),
      radial-gradient(ellipse 46% 52% at 50% 42%,var(--coat-tan) 0%,rgba(217,164,102,.7) 50%,rgba(217,164,102,0) 100%),
      radial-gradient(ellipse 70% 40% at 50% 88%,rgba(236,228,205,.8) 0%,rgba(236,228,205,0) 100%);
  }

  .brand-tab{position:absolute;left:50%;transform:translateX(-50%);top:0;width:172px;height:97px;}
  .brand-tab svg{position:absolute;inset:0;}
  .brand-tab-name{
    position:absolute;left:0;right:0;top:20px;display:flex;align-items:center;justify-content:center;gap:6px;
    color:var(--brand-teal);font-weight:600;font-size:15px;line-height:1.05;text-align:left;
  }
  .brand-tab-name i{display:block;width:26px;height:26px;background:var(--brand-teal);flex:none;}

  .product-title{
    position:absolute;left:0;right:0;top:116px;text-align:center;
    font-family:"Rye",serif;font-weight:400;color:var(--title-green);line-height:1;
    text-shadow:
      2px 0 0 var(--title-outline),-2px 0 0 var(--title-outline),
      0 2px 0 var(--title-outline),0 -2px 0 var(--title-outline),
      1.5px 1.5px 0 var(--title-outline),-1.5px -1.5px 0 var(--title-outline),
      1.5px -1.5px 0 var(--title-outline),-1.5px 1.5px 0 var(--title-outline);
  }
  .product-title span{display:block;font-size:60px;height:90px;line-height:90px;transform:scaleY(1.35);}

  .benefit-badge{
    position:absolute;left:42px;width:354px;top:318px;height:70px;border-radius:14px;
    background:var(--badge-navy);color:var(--white);
    font-weight:600;font-size:27px;line-height:31px;text-align:center;padding-top:4px;letter-spacing:.5px;
  }
  .spec-lines{
    position:absolute;left:0;right:0;top:394px;text-align:center;color:var(--white);
    font-weight:500;font-size:16px;line-height:19px;
  }
  .spec-rule{width:250px;height:1px;background:var(--white);margin:6px auto 7px;}
  .claim-lines{font-weight:600;font-size:14.5px;line-height:16.5px;}

  .origin{position:absolute;left:42px;top:741px;display:flex;align-items:center;gap:4px;}
  .origin-flag{display:block;width:59px;height:30px;}
  .origin-text{color:var(--flag-red);font-family:"Roboto",sans-serif;font-size:12px;line-height:13px;border-left:1px solid var(--flag-red);padding-left:3px;}
  .volume{position:absolute;right:44px;top:746px;color:var(--white);font-weight:600;font-size:16px;}

  /* logo presentation */
  .logo-heading{
    position:absolute;left:700px;width:380px;top:108px;text-align:center;
    color:var(--white);font-family:"Roboto",sans-serif;font-weight:400;font-size:38px;
  }
  .brand-logo{position:absolute;left:660px;top:222px;display:flex;align-items:center;gap:18px;}
  .brand-logo i{display:block;width:96px;height:96px;background:var(--brand-teal);flex:none;}
  .brand-logo span{color:var(--brand-teal);font-weight:600;font-size:48px;line-height:50px;}
</style>
</head>
<body>

  <div class="dimension dimension-width">
    <svg width="440" height="40" viewBox="0 0 440 40">
      <line x1="0" y1="0" x2="0" y2="40" stroke="#2b6fa8" stroke-width="1.5"/>
      <line x1="440" y1="0" x2="440" y2="40" stroke="#2b6fa8" stroke-width="1.5"/>
      <line x1="4" y1="20" x2="130" y2="20" stroke="#2b6fa8" stroke-width="1.5"/>
      <line x1="310" y1="20" x2="436" y2="20" stroke="#2b6fa8" stroke-width="1.5"/>
      <polygon points="2,20 26,14 26,26" fill="#2b6fa8"/>
      <polygon points="438,20 414,14 414,26" fill="#2b6fa8"/>
    </svg>
    <div class="dimension-value">6.20 cm</div>
  </div>

  <div class="dimension dimension-height">
    <svg width="40" height="922" viewBox="0 0 40 922">
      <line x1="0" y1="0" x2="40" y2="0" stroke="#2b6fa8" stroke-width="1.5"/>
      <line x1="0" y1="922" x2="40" y2="922" stroke="#2b6fa8" stroke-width="1.5"/>
      <line x1="20" y1="4" x2="20" y2="370" stroke="#2b6fa8" stroke-width="1.5"/>
      <line x1="20" y1="552" x2="20" y2="918" stroke="#2b6fa8" stroke-width="1.5"/>
      <polygon points="20,2 14,26 26,26" fill="#2b6fa8"/>
      <polygon points="20,920 14,896 26,896" fill="#2b6fa8"/>
    </svg>
    <div class="dimension-value">13.00 cm</div>
  </div>

  <section class="label">
    <div class="label-backdrop"></div>
    <div class="label-photo" role="img" aria-label="Photograph of a smiling corgi lying in sunlit grass, wearing a green collar"></div>

    <div class="brand-tab">
      <svg width="172" height="97" viewBox="0 0 172 97"><polygon points="0,0 172,0 172,78 86,97 0,78" fill="#ffffff"/></svg>
      <div class="brand-tab-name"><i></i><span>Brightwell<br>Essence</span></div>
    </div>

    <h1 class="product-title">
      <span>COLLOIDAL</span>
      <span>SILVER</span>
    </h1>

    <div class="benefit-badge">NATURAL FIRST AID<br>FOR PETS</div>

    <div class="spec-lines">
      <p>10 PPM - No Preservaties</p>
      <p>100% Pure - No Additives</p>
      <div class="spec-rule"></div>
      <div class="claim-lines">
        <p>Anti microbial, Anti Fungal,</p>
        <p>Anti Bacterial, Anti Viral</p>
        <p>Treats burns, Bites, Cuts, Abrasions,</p>
        <p>Hots Spots</p>
      </div>
    </div>

    <div class="origin">
      <svg class="origin-flag" viewBox="0 0 60 30" aria-label="Canadian flag">
        <rect width="60" height="30" fill="#ffffff"/>
        <rect width="15" height="30" fill="#e0222b"/>
        <rect x="45" width="15" height="30" fill="#e0222b"/>
        <path fill="#e0222b" d="M30 4 l2 4 2.5-1 -1 6 3-3 .8 2 3.2-.6 -1 3.4 1.5.8 -5.5 4.6 .6 2 -5.2-.8 V27 h-1.8 v-4.6 l-5.2.8 .6-2 -5.5-4.6 1.5-.8 -1-3.4 3.2.6 .8-2 3 3 -1-6 2.5 1z"/>
      </svg>
      <div class="origin-text">MADE IN<br>CANADA</div>
    </div>
    <div class="volume">8 oz / 250 ml</div>
  </section>

  <h2 class="logo-heading">New Logo</h2>
  <div class="brand-logo"><i></i><span>Brightwell<br>Essence</span></div>

</body>
</html>
```